Cover Art for Podcast called Ahoy There Swift Otters, Badgers, Minnows!

I need this graphic to be 3000 px square at 300 DPI but it should be legible even if only 300 px square online. This will be cover Art for Podcast called Ahoy There Swift Otters, Badgers, Minnows! but may also be used on merch for the non profit featured in the show.

```html
<!DOCTYPE html>
<html lang="en">
<head>
<meta charset="utf-8">
<title>Ahoy There Swift Otters, Badgers, Minnows! – Podcast Cover</title>
<link rel="stylesheet" href="https://fonts.googleapis.com/css2?family=Fredoka:wght@700&display=swap">
<style>
  :root {
    --page: #ffffff;
    --navy-deep: #0b1e2c;
    --navy-edge: #163149;
    --sun: #fbb016;
    --ember: #e2401a;
    --chalk: #ffffff;
    --ghost: #1d3446;
  }
  html, body {
    margin: 0;
    padding: 0;
    width: 1200px;
    height: 1200px;
    overflow: hidden;
    background: var(--page);
  }
  .board {
    position: relative;
    width: 1200px;
    height: 1200px;
  }
  .cover-preview {
    position: absolute;
    display: block;
  }
  .cover-preview--full   { left: 277px; top: 131px;  width: 604px; height: 604px; }
  .cover-preview--large  { left: 277px; top: 775px;  width: 302px; height: 302px; }
  .cover-preview--medium { left: 614px; top: 926px;  width: 151px; height: 151px; }
  .cover-preview--small  { left: 794px; top: 1002px; width: 75px;  height: 75px; }
  .cover-preview--icon   { left: 894px; top: 1041px; width: 36px;  height: 36px; }

  .title-type {
    font-family: "Fredoka", "Arial Rounded MT Bold", sans-serif;
    font-weight: 700;
  }
  .title-line--sun   { fill: var(--sun); }
  .title-line--chalk { fill: var(--chalk); }
  .title-shadow      { fill: var(--ember); }
  .accent-rule       { stroke: var(--ember); stroke-width: 4; }
  .podcast-label {
    fill: var(--sun);
    font-family: "Fredoka", "Arial Rounded MT Bold", sans-serif;
    font-weight: 700;
    font-size: 24px;
    letter-spacing: 26px;
  }
  .mascot-area { fill: var(--ghost); opacity: 0.35; }
  .cover-bg-edge  { stop-color: var(--navy-edge); }
  .cover-bg-core  { stop-color: var(--navy-deep); }
</style>
</head>
<body>
<main class="board">

  <svg class="cover-preview cover-preview--full" viewBox="0 0 604 604" role="img" aria-label="Ahoy There Swift Otters, Badgers, Minnows! podcast cover">
    <defs>
      <radialGradient id="cover-bg" cx="50%" cy="55%" r="75%">
        <stop offset="0%" class="cover-bg-core"/>
        <stop offset="60%" class="cover-bg-core"/>
        <stop offset="100%" class="cover-bg-edge"/>
      </radialGradient>
      <symbol id="cover" viewBox="0 0 604 604">
        <rect class="cover-background" width="604" height="604" fill="url(#cover-bg)"/>

        <rect class="mascot-area" x="236" y="479" width="131" height="115" rx="40"
              role="img" aria-label="Faint line drawing of two animal mascots sitting together"/>

        <g class="title-type" transform="rotate(-3 302 302)">
          <text class="title-line--sun" x="54" y="168" font-size="92" textLength="480" lengthAdjust="spacingAndGlyphs">AHOY THERE</text>

          <line class="accent-rule" x1="60" y1="203" x2="212" y2="203"/>
          <text class="title-line--sun" x="62" y="252" font-size="46" textLength="148" lengthAdjust="spacingAndGlyphs">SWIFT</text>
          <line class="accent-rule" x1="60" y1="266" x2="212" y2="266"/>

          <text class="title-shadow" x="222" y="266" font-size="100" textLength="318" lengthAdjust="spacingAndGlyphs">OTTERS,</text>
          <text class="title-line--chalk" x="218" y="262" font-size="100" textLength="318" lengthAdjust="spacingAndGlyphs">OTTERS,</text>

          <text class="title-shadow" x="74" y="376" font-size="106" textLength="466" lengthAdjust="spacingAndGlyphs">BADGERS,</text>
          <text class="title-line--chalk" x="70" y="372" font-size="106" textLength="466" lengthAdjust="spacingAndGlyphs">BADGERS<tspan class="title-line--sun">,</tspan></text>

          <text class="title-shadow" x="76" y="476" font-size="100" textLength="468" lengthAdjust="spacingAndGlyphs">MINNOWS!</text>
          <text class="title-line--chalk" x="72" y="472" font-size="100" textLength="468" lengthAdjust="spacingAndGlyphs">MINNOWS!</text>
        </g>

        <text class="podcast-label" x="315" y="549" text-anchor="middle">PODCAST</text>
      </symbol>
    </defs>
    <use href="#cover"/>
  </svg>

  <svg class="cover-preview cover-preview--large" viewBox="0 0 604 604" role="img" aria-label="Cover at medium size"><use href="#cover"/></svg>
  <svg class="cover-preview cover-preview--medium" viewBox="0 0 604 604" role="img" aria-label="Cover at small size"><use href="#cover"/></svg>
  <svg class="cover-preview cover-preview--small" viewBox="0 0 604 604" role="img" aria-label="Cover at thumbnail size"><use href="#cover"/></svg>
  <svg class="cover-preview cover-preview--icon" viewBox="0 0 604 604" role="img" aria-label="Cover at icon size"><use href="#cover"/></svg>

</main>
</body>
</html>
```